an author seeking a cool ebook cover design

We need an ebook cover design for an old book I'd written 10yrs ago so that I can make it into an ebook. It's a self help health and wellbeing book, that covers everything from fitness, nutrition to mediation and stress management.

I'd like to see designs that use a toolbox (i have attached a photo I'd like to use (no need for stock photo as it's my toolbox and photo).

The cover should be clear and easy to read.

here's a description of what's inside the book (i've also attached a rough pdf of insides)
Ona’s Quiet Satchel is full of all the practical tips you need to help get you thinking straight, feeling great and looking great.

This concise books saves you time by finding the right tool you need for your own personal challenge, be it physical, mental or energetic. It’s practical, fun, easy to read and most of all it’s effective.

Toby Marquand brings all his experience and knowledge and bundles it all together to give you a book that is in many ways the ‘bramble quarterly’ on lifestyle! It will help you turn every day dramas and challenges into remarkable successes.

The three main parts to this book are essential to living: The mind, the body and the spirit. You will learn how to meditate, stretch, exercise, eat well to live longer, choose a new direction in life, deal with stress, use acupressure for illness and learn how to clear a cluttered mind and transform it into a happy and content one.

Target Market(s)

25- 40yr old mostly female

Industry/Entity Type

Nutrition

Requirements
Must have
• must have:
the author name - Toby Marquand
Book title - Ona's Quiet Satchel
bi line - quick tips for a happier healthier you
picture of toolbox
must have specs:

1,600 pixels wide by 2,400 pixels tall or similar ratio. The image must be at least 1,600 pixels wide, and the height should be greater than the width.
image must be in RGB color, not CMYK
file type to be jpeg - maximum file size 18MB
Nice to have
• like to see more of hand written font style like 'sketch nice' if possible

```html
<!DOCTYPE html>
<html lang="en">
<head>
<meta charset="utf-8">
<title>Ona's Quiet Satchel — Toby Marquand</title>
<link rel="stylesheet" href="https://fonts.googleapis.com/css2?family=Yesteryear&family=Damion&family=Kaushan+Script&display=swap">
<style>
  :root {
    --olive: #b9a042;
    --gold: #e6ad0b;
    --green: #4f8842;
    --stripe: #ffffff;
    --title-red: #e3121c;
    --box-red: #d8322a;
    --box-red-dark: #a8221c;
    --ink-white: #ffffff;
    --shadow: rgba(40, 30, 0, 0.55);
  }
  html, body {
    margin: 0;
    padding: 0;
    overflow: hidden;
    background: #ffffff;
  }
  .cover {
    position: relative;
    width: 800px;
    height: 1200px;
    overflow: hidden;
  }
  .cover-bands {
    position: absolute;
    inset: 0;
  }
  .toolbox-photo {
    position: absolute;
    left: 0;
    top: 0;
  }
  .title {
    position: absolute;
    left: 0;
    width: 800px;
    margin: 0;
    font-family: "Yesteryear", cursive;
    font-weight: 400;
    color: var(--title-red);
    font-size: 128px;
    line-height: 1;
    white-space: nowrap;
    -webkit-text-stroke: 14px var(--stripe);
    paint-order: stroke fill;
  }
  .title-line { position: absolute; white-space: nowrap; }
  .title-line--one { left: 62px; top: 120px; }
  .title-line--two { left: 205px; top: 290px; }
  .byline {
    position: absolute;
    margin: 0;
    font-family: "Damion", cursive;
    color: var(--ink-white);
    font-size: 64px;
    line-height: 1;
    text-shadow: 3px 3px 3px var(--shadow);
    white-space: nowrap;
  }
  .byline--one { left: 205px; top: 520px; }
  .byline--two { left: 158px; top: 597px; }
  .byline--three { left: 510px; top: 684px; }
  .author {
    position: absolute;
    left: 0;
    width: 800px;
    top: 1110px;
    margin: 0;
    text-align: center;
    font-family: "Kaushan Script", cursive;
    color: var(--ink-white);
    font-size: 62px;
    line-height: 1;
    white-space: nowrap;
  }
</style>
</head>
<body>
<main class="cover">
  <svg class="cover-bands" width="800" height="1200" viewBox="0 0 800 1200" aria-hidden="true">
    <rect width="800" height="1200" fill="var(--gold)"/>
    <polygon points="0,0 800,0 800,85 115,462 0,385" fill="var(--olive)"/>
    <polygon points="0,385 800,930 800,1200 270,1200 0,1010" fill="var(--green)"/>
    <line x1="115" y1="462" x2="800" y2="85" stroke="var(--stripe)" stroke-width="9"/>
    <line x1="0" y1="385" x2="800" y2="930" stroke="var(--stripe)" stroke-width="9"/>
    <line x1="0" y1="1010" x2="270" y2="1200" stroke="var(--stripe)" stroke-width="9"/>
  </svg>

  <svg class="toolbox-photo" width="800" height="1200" viewBox="0 0 800 1200" role="img" aria-label="Photograph of the author's worn red metal toolbox, lid slightly open">
    <rect x="95" y="690" width="585" height="340" rx="34" fill="var(--stripe)"/>
    <rect x="104" y="699" width="567" height="322" rx="28" fill="var(--box-red)"/>
    <rect x="104" y="880" width="567" height="60" fill="var(--box-red-dark)"/>
  </svg>

  <h1 class="title">
    <span class="title-line title-line--one">Ona’s Quiet</span>
    <span class="title-line title-line--two">Satchel</span>
  </h1>

  <p class="byline byline--one">quick tips for a</p>
  <p class="byline byline--two">happier healthier</p>
  <p class="byline byline--three">you</p>

  <p class="author">Toby Marquand</p>
</main>
</body>
</html>
```